Geschäftspapiere
Zielgruppe
Die TIVA Salbe gibt ein zuverlässige Gefühl, durch ein innovatives Naturprodukt erstaunlich schnelle, wirkungsvolle Hilfe bei Schmerzen des Bewegungsapparates und bei Hautschäden zu erhalten und dabei gleichzeitig die Haut zu pflegen.
Wir wollen jetzt stärker auf die Zielgruppe TCM Praxis, Chiropraktiker, Physiotherapie gehen und wollen nun eine Preisliste dafür erstellen.
Aufgabenstellung
Zielgruppe ist B2B, TCM Praxis, Chiropraktiker, Physiotherapie.
Die Preisliste sollte auf den Briefpapier erstellt werden. Bitte an Farben, Logos etc. von der Webseite nehmen.

```html
<!DOCTYPE html>
<html lang="de">
<head>
<meta charset="utf-8">
<title>Preisliste – Lumen Tiva</title>
<link href="https://fonts.googleapis.com/css2?family=Source+Sans+3:wght@400;600;700;900&display=swap" rel="stylesheet">
<style>
  :root{
    --bg:#e8ebe9;
    --paper:#f4f4f5;
    --orange:#e5a00d;
    --orange-dark:#d38f05;
    --gray-card:#7a7a7e;
    --gray-card-light:#9a9a9e;
    --black-card:#1b1b1b;
    --text:#5b5b60;
    --white:#ffffff;
  }
  *{box-sizing:border-box;margin:0;padding:0}
  html,body{width:1200px;height:1012px;overflow:hidden}
  body{background:var(--bg);font-family:"Source Sans 3",sans-serif;color:var(--text);position:relative}
  .sheet{position:absolute;left:263px;top:24px;width:676px;height:965px;background:var(--paper);overflow:hidden;box-shadow:0 12px 30px rgba(0,0,0,.18)}
  .edge-line{position:absolute;left:672px;top:0;width:3px;height:100%;background:var(--orange)}
  .logo-disc{position:absolute;left:430px;top:-54px;width:226px;height:226px;border-radius:50%;background:#f7f7f8;box-shadow:0 4px 8px rgba(0,0,0,.22)}
  .brand{position:absolute;left:462px;top:44px;width:170px}
  .brand-row{display:flex;align-items:center;gap:8px}
  .brand-dot{width:34px;height:34px;border-radius:50%;background:var(--orange)}
  .brand-name{font-size:44px;font-weight:900;line-height:1;color:#111;letter-spacing:-1px}
  .brand-sub{margin:8px 0 0 44px;font-size:12px;letter-spacing:2px;color:#555}
  .brand-claim{margin:8px 0 0 44px;font-size:12px;letter-spacing:1.2px;font-weight:600;color:var(--orange)}
  .sender{position:absolute;left:79px;top:157px;font-size:7px;color:#666}
  .sender b{font-weight:700}
  .title-rule{position:absolute;left:0;top:288px;width:170px;height:1.5px;background:var(--orange)}
  .side-tick{position:absolute;left:0;top:339px;width:12px;height:1.5px;background:var(--orange)}
  .title{position:absolute;left:79px;top:271px;font-size:14px;font-weight:700;color:var(--orange)}
  .intro{position:absolute;left:79px;top:298px;width:548px;font-size:10.5px;line-height:18px}
  .card{position:absolute;top:420px;width:142px;height:362px;border-radius:12px 12px 50% 50% / 12px 12px 22px 22px;color:var(--white);text-align:center}
  .card--starter{left:79px;background:linear-gradient(180deg,var(--gray-card-light),var(--gray-card) 30%)}
  .card--premium{left:271px;background:linear-gradient(180deg,#3a3a3a,var(--black-card) 30%)}
  .card--special{left:462px;background:linear-gradient(180deg,#f2b836,var(--orange) 30%)}
  .card-badge{position:absolute;left:26px;top:-32px;width:90px;height:90px;border-radius:50%;background:var(--white);border:4px solid #d9a528;box-shadow:0 2px 4px rgba(0,0,0,.25)}
  .card-band{position:absolute;left:0;top:74px;width:100%;height:24px;font-size:18px;font-weight:700;line-height:24px;letter-spacing:.5px}
  .card--starter .card-band,.card--premium .card-band{background:var(--orange)}
  .card--special .card-band{background:#111}
  .card-qty{position:absolute;top:114px;width:100%;font-size:17px;font-weight:600}
  .card-rule{position:absolute;left:10px;width:122px;height:1.5px;background:rgba(255,255,255,.85)}
  .card-price{position:absolute;top:160px;width:100%;font-size:15px;font-weight:600}
  .card-text{position:absolute;top:396px;top:196px;left:10px;width:122px;font-size:8.5px;font-weight:600;line-height:17px}
  .footer{position:absolute;left:0;top:862px;width:655px;height:68px;background:var(--orange);color:var(--white);font-size:7.5px;line-height:12.8px;padding:8px 0 0 37px;display:flex}
  .footer-col{padding-right:10px}
  .footer-col+.footer-col{border-left:1px solid rgba(255,255,255,.85);padding-left:7px}
  .footer-col b{font-weight:700}
  .c1{width:131px}.c2{width:180px}.c3{width:157px}
  .badges{position:absolute;left:0;top:934px;width:655px;height:31px;background:var(--orange);display:flex;align-items:center;justify-content:space-around;padding:0 50px}
  .badge{width:18px;height:18px;border-radius:50%;background:#f0ece4;border:2px solid #a8761a}
  .badge.wide{width:34px;height:8px;border-radius:1px}
</style>
</head>
<body>
<main class="sheet">
  <div class="edge-line"></div>
  <div class="logo-disc"></div>
  <div class="brand">
    <div class="brand-row"><span class="brand-dot"></span><span class="brand-name">TIVA</span></div>
    <div class="brand-sub">NATURBALSAME</div>
    <div class="brand-claim">LUMEN TIVA</div>
  </div>

  <p class="sender"><b>Hallberg Medical Vertrieb GmbH</b> · Lindenhofstr. 7 · 80331 München</p>

  <div class="title-rule"></div>
  <div class="side-tick"></div>
  <h1 class="title">PREISLISTE:</h1>
  <p class="intro">Lorem ipsum dolor sit amet, consectetuer adipiscing elit, sed diam nonummy nibh euismod tincidunt ut laoreet dolore magna aliquam erat volutpat. Ut wisi enim ad minim veniam, quis nostrud exerci tation ullamcorper suscipit lobortis</p>

  <section class="card card--starter">
    <div class="card-badge"></div>
    <div class="card-band">STARTER</div>
    <div class="card-qty">5 Tuben</div>
    <div class="card-rule" style="top:148px"></div>
    <div class="card-price">20,99 €</div>
    <div class="card-rule" style="top:190px"></div>
    <p class="card-text">Tiva Naturbalsam ist ein natürliches Wohlfühlpro­gramm für Muskeln, Gelenke, Knochen, Nerven, Sehnen und Bänder sowie bei Prellungen und Verbrennungen. Betroffene können die entspannende</p>
  </section>

  <section class="card card--premium">
    <div class="card-badge"></div>
    <div class="card-band">PREMIUM</div>
    <div class="card-qty">20 Tuben</div>
    <div class="card-rule" style="top:148px"></div>
    <div class="card-price">20,99 €</div>
    <div class="card-rule" style="top:190px"></div>
    <p class="card-text">Tiva Naturbalsam ist ein natürliches Wohlfühlpro­gramm für Muskeln, Gelenke, Knochen, Nerven, Sehnen und Bänder sowie bei Prellungen und Verbrennungen. Betroffene können die entspannende</p>
  </section>

  <section class="card card--special">
    <div class="card-badge"></div>
    <div class="card-band">SPECIAL</div>
    <div class="card-qty">50 Tuben</div>
    <div class="card-rule" style="top:148px"></div>
    <div class="card-price">20,99 €</div>
    <div class="card-rule" style="top:190px"></div>
    <p class="card-text">Tiva Naturbalsam ist ein natürliches Wohlfühlpro­gramm für Muskeln, Gelenke, Knochen, Nerven, Sehnen und Bänder sowie bei Prellungen und Verbrennungen. Betroffene können die entspannende</p>
  </section>

  <footer class="footer">
    <div class="footer-col c1"><b>Hallberg Medical Vertrieb GmbH</b><br>Lindenhofstr. 7<br>80331 München<br>Deutschland</div>
    <div class="footer-col c2"><b>Telefon:</b> 0049 89 312 540 21<br><b>Telefax:</b> 0049 89 312 540 22<br><b>E-Mail:</b> bestellung@tiva-naturbalsam.de<br><b>Internet:</b> www.tiva-naturbalsam.de</div>
    <div class="footer-col c3"><b>Gesellschafter:</b> Jonas Reiter<br>Gesellschaft mit beschränkter Haftung<br>Amtsgericht München | HRB 318702<br><b>St.-Nr.:</b> 146/221/40517</div>
    <div class="footer-col">Nordbank<br><b>IBAN</b> DE12 7005 0000 0412 6638 10<br><b>BIC</b> NORBDEMMXXX</div>
  </footer>
  <div class="badges">
    <span class="badge"></span><span class="badge"></span><span class="badge"></span><span class="badge"></span><span class="badge"></span><span class="badge"></span><span class="badge wide"></span>
  </div>
</main>
</body>
</html>
```